Event Poster Design for Camp for Teenagers

I need graphics designed for our summer camps event. These camps are for teenagers, 6-12th grades. Primary graphic design is for a 11x17 poster but will also need the images resized for social, 16x9 title slide, and a postcard size. Graphic should include the following:Main Title: Ridgeway Youthline Summer CampsDates: High School - June 3-7; Middle School - June 17-21; Merge - June 24 - 28Register at SDNextGen.comFor each camp, include name and headshot of speaker:High: Liam Brevik (guy in blue shirt)Middle: Marla Penhow (girl)Merge: Joey SilvaInclude Ridgeway Youthline logoBlack Hills Retreat Center, Deadwood, SDGraphic should be attractive to teenagers. Ideas - geometric shapes, 90's coloring/imagery, bright colors, soft earth tones, etc. Open to ideasMy graphic design experience is VERY limited. I will need help receiving the files I need in the various sizes. Thank you.

```html
<!DOCTYPE html>
<html lang="en">
<head>
<meta charset="utf-8">
<title>Ridgeway Youthline Summer Camps</title>
<link rel="stylesheet" href="https://fonts.googleapis.com/css2?family=Jost:wght@400;500;600&display=swap">
<style>
  :root {
    --page: #ecebe6;
    --sky-top: #3a7fc0;
    --sky-mid: #8fb8de;
    --forest: #2f4a4a;
    --band: #2484c0;
    --lilac: #a79ce0;
    --pink: #e98fd5;
    --hex: #5a86b8;
    --tri-dark: #4676ab;
    --tri-bright: #2b8dc4;
    --tri-edge: #8fd0ee;
    --portrait: #1c1c22;
    --white: #ffffff;
    --ink: #111111;
  }
  * { margin: 0; padding: 0; box-sizing: border-box; }
  html, body { width: 1200px; height: 1200px; overflow: hidden; }
  body {
    background: var(--page);
    font-family: "Jost", "Helvetica Neue", Arial, sans-serif;
    position: relative;
  }
  .poster {
    position: absolute;
    left: 231px; top: 30px;
    width: 738px; height: 1140px;
    overflow: hidden;
    background: linear-gradient(180deg, var(--lilac) 0%, #c295e0 55%, var(--pink) 100%);
  }
  .hero {
    position: absolute; left: 0; top: 0; width: 738px; height: 390px;
    background: linear-gradient(180deg, var(--sky-top) 0%, var(--sky-mid) 42%, #6f8fa8 62%, var(--forest) 100%);
  }
  .brand {
    position: absolute; left: 10px; top: 14px;
    display: flex; align-items: center; gap: 6px;
    color: var(--white); font-weight: 600; font-size: 15px;
  }
  .brand-mark { width: 14px; height: 14px; background: var(--band); }
  .hero-title {
    position: absolute; left: 0; width: 100%; top: 140px;
    text-align: center; color: var(--white);
    font-weight: 500; font-size: 56px; line-height: 1;
  }
  .hero-subtitle {
    position: absolute; left: 0; width: 100%; top: 230px;
    text-align: center; color: var(--white);
    font-weight: 500; font-size: 46px; line-height: 1;
  }
  .register-button {
    position: absolute; left: 236px; top: 297px; width: 270px; height: 57px;
    background: var(--white); color: var(--ink);
    display: flex; align-items: center; justify-content: center;
    font-weight: 500; font-size: 36px;
  }
  .register-band {
    position: absolute; left: 0; top: 390px; width: 738px; height: 66px;
    background: var(--band); color: var(--white);
    display: flex; align-items: center; justify-content: center;
    font-weight: 500; font-size: 31px;
  }
  .action-photo {
    position: absolute; left: 0; top: 456px; width: 738px; height: 684px;
    background: radial-gradient(ellipse at 62% 40%, rgba(90,80,140,0.35) 0%, rgba(0,0,0,0) 55%),
                linear-gradient(180deg, rgba(0,0,0,0) 70%, rgba(150,60,140,0.35) 100%);
  }
  .lineup { position: absolute; left: 0; top: 0; width: 738px; height: 1140px; }
  .lineup text { font-family: "Jost", "Helvetica Neue", Arial, sans-serif; fill: var(--white); text-anchor: middle; font-weight: 500; }
  .speaker-name { font-size: 20px; }
  .speaker-camp { font-size: 26px; }
  .speaker-dates { font-size: 13px; }
  .section-title { font-size: 40px; }
  .camp-date { font-size: 28px; }
  .camp-label { font-size: 17px; }
</style>
</head>
<body>
  <main class="poster">
    <section class="hero" role="img" aria-label="Mountain lake landscape with forest under a blue sky with clouds">
      <div class="brand"><span class="brand-mark"></span>Ridgeway Youthline</div>
      <h1 class="hero-title">Ridgeway Youthline</h1>
      <h2 class="hero-subtitle">Summer Camps</h2>
      <div class="register-button">Register Now</div>
    </section>
    <div class="register-band">Register at RidgewayYouthline.com</div>
    <div class="action-photo" role="img" aria-label="Teen skateboarders at a skate park, tinted purple and pink"></div>

    <svg class="lineup" viewBox="0 0 738 1140" xmlns="http://www.w3.org/2000/svg">
      <!-- speaker hexagons -->
      <polygon class="speaker-hex" fill="var(--hex)" points="77,474 211,474 278,610 211,746 77,746 10,610"/>
      <polygon class="speaker-hex" fill="var(--hex)" points="292,611 430,611 497,746 430,881 292,881 225,746"/>
      <polygon class="speaker-hex" fill="var(--hex)" points="77,757 211,757 278,892 211,1028 77,1028 10,892"/>

      <circle cx="144" cy="558" r="82" fill="var(--portrait)" role="img" aria-label="Portrait of speaker Danny Obert with partner"/>
      <circle cx="361" cy="694" r="80" fill="var(--portrait)" role="img" aria-label="Portrait of speaker Marla Penhow"/>
      <circle cx="146" cy="845" r="80" fill="var(--portrait)" role="img" aria-label="Portrait of speaker Liam Brevik"/>

      <text class="speaker-name" x="144" y="668">Danny Obert</text>
      <text class="speaker-camp" x="144" y="709">MergeSchool</text>
      <text class="speaker-dates" x="144" y="736">Dates : June 24-28</text>

      <text class="speaker-name" x="361" y="808">Marla Penhow</text>
      <text class="speaker-camp" x="361" y="845">MiddleSchool</text>
      <text class="speaker-dates" x="361" y="871">Dates : June 17-21</text>

      <text class="speaker-name" x="146" y="952">Liam Brevik</text>
      <text class="speaker-camp" x="146" y="991">HighSchool</text>
      <text class="speaker-dates" x="146" y="1021">Dates : June 3-7</text>

      <text class="section-title" x="573" y="568">Honorable</text>
      <text class="section-title" x="573" y="628">Speaker</text>

      <!-- camp date triangles -->
      <polygon fill="var(--tri-dark)" points="293,910 502,910 403,1116"/>
      <polygon fill="var(--tri-dark)" points="516,910 723,910 617,1116"/>
      <polygon fill="var(--tri-bright)" stroke="var(--tri-edge)" stroke-width="3" points="508,907 617,1116 403,1116"/>

      <text class="camp-date" x="397" y="962">June 3-7</text>
      <text class="camp-label" x="397" y="988">HighSchool</text>

      <text class="camp-date" x="620" y="953">June 17-24</text>
      <text class="camp-label" x="620" y="980">MiddleSchool</text>

      <text class="camp-label" x="508" y="1059">MergeSchool</text>
      <text class="camp-date" x="508" y="1094">June 24-28</text>
    </svg>
  </main>
</body>
</html>
```